Life Coach for Lawyers Business Card Design

Elegant, original, business card design for life coaching service for associate attorneys who work in big law and struggle with stress, overwhelm, and time management. Double sided design.

Target Market(s)

Women associate attorneys who work in big law and struggle with stress, overwhelm, and time management.

Industry/Entity Type

Life Coaching

Contact Information for Business Card

Marlene Quorthby
Life Coach
519.607.4431
brightcounselpath.net
marlene@brightcounselpath.net
@brightcounselpath (Instagram)

Font styles to use
Other font styles liked:
• Silver South font duo. See uploaded files.

Requirements
Must have
• Icons for phone, website, email, and Instagram instead of words. Specific colors used in my logo (171B2B, 421121, FFFFFF)
Nice to have
• Foil. Embossed. Feminine design.
Should not have
• Any colors other than those used in logo. See uploaded files.

```html
<!DOCTYPE html>
<html lang="en">
<head>
<meta charset="utf-8">
<title>Bright Counsel Path – Business Card</title>
<link rel="stylesheet" href="https://fonts.googleapis.com/css2?family=Comfortaa:wght@500&family=Lora:wght@400&family=Playfair+Display:wght@400&display=swap">
<style>
  :root {
    --navy: #171B2B;
    --wine: #421121;
    --white: #FFFFFF;
    --page: #F4F3F3;
  }
  * { margin: 0; padding: 0; box-sizing: border-box; }
  html, body { width: 1200px; height: 1200px; overflow: hidden; background: var(--page); }
  .canvas { position: relative; width: 1200px; height: 1200px; }

  .card { position: absolute; left: 188px; width: 824px; height: 494px; }
  .card-front { top: 74px; background: var(--white); }
  .card-back { top: 635px; background: var(--wine); }

  .brand-name {
    position: absolute; left: 56px; top: 66px;
    font-family: "Playfair Display", Georgia, serif;
    font-weight: 400; font-size: 40px; line-height: 1.05;
    color: var(--wine); letter-spacing: 1px;
  }

  .person-name {
    position: absolute; left: 56px; top: 212px;
    font-family: "Comfortaa", Arial, sans-serif;
    font-weight: 500; font-size: 35px; color: var(--navy);
  }
  .person-role {
    position: absolute; left: 57px; top: 255px;
    font-family: "Comfortaa", Arial, sans-serif;
    font-weight: 500; font-size: 20px; letter-spacing: 4px; color: var(--wine);
  }

  .contact-list { position: absolute; left: 56px; top: 308px; list-style: none; }
  .contact-item {
    display: flex; align-items: center; height: 36.5px;
    font-family: "Lora", Georgia, serif; font-size: 22px; color: var(--navy);
  }
  .contact-icon { width: 22px; height: 22px; margin-right: 23px; flex: none; }

  .seal {
    position: absolute; left: 268px; top: 103px; width: 288px; height: 288px;
    border: 2px solid var(--white); border-radius: 50%;
    display: flex; align-items: center; justify-content: center; text-align: center;
  }
  .seal-name {
    font-family: "Playfair Display", Georgia, serif;
    font-weight: 400; font-size: 30px; line-height: 1.2;
    color: var(--white); letter-spacing: 2px;
  }
</style>
</head>
<body>
<main class="canvas">
  <section class="card card-front" aria-label="Card front">
    <div class="brand-name">Bright Counsel<br>Path</div>

    <h1 class="person-name">Marlene Quorthby</h1>
    <p class="person-role">LIFE COACH</p>

    <ul class="contact-list">
      <li class="contact-item">
        <svg class="contact-icon" viewBox="0 0 22 22" aria-hidden="true">
          <rect x="5" y="1" width="12" height="20" rx="2" fill="none" stroke="var(--wine)" stroke-width="2"/>
          <rect x="7" y="3" width="8" height="13" fill="var(--wine)"/>
        </svg>
        519.607.4431
      </li>
      <li class="contact-item">
        <svg class="contact-icon" viewBox="0 0 22 22" aria-hidden="true">
          <path d="M2 9 L11 3 L20 9 V19 H2 Z" fill="none" stroke="var(--wine)" stroke-width="2" stroke-linejoin="round"/>
          <path d="M2 9 L11 15 L20 9" fill="none" stroke="var(--wine)" stroke-width="2" stroke-linejoin="round"/>
        </svg>
        marlene@brightcounselpath.net
      </li>
      <li class="contact-item">
        <svg class="contact-icon" viewBox="0 0 22 22" aria-hidden="true">
          <circle cx="11" cy="11" r="9" fill="none" stroke="var(--wine)" stroke-width="2"/>
        </svg>
        brightcounselpath
      </li>
      <li class="contact-item">
        <svg class="contact-icon" viewBox="0 0 22 22" aria-hidden="true">
          <circle cx="11" cy="11" r="10" fill="var(--wine)"/>
          <g fill="none" stroke="var(--white)" stroke-width="1.2">
            <ellipse cx="11" cy="11" rx="4" ry="10"/>
            <line x1="1" y1="11" x2="21" y2="11"/>
            <line x1="3" y1="6" x2="19" y2="6"/>
            <line x1="3" y1="16" x2="19" y2="16"/>
          </g>
        </svg>
        brightcounselpath.net
      </li>
    </ul>
  </section>

  <section class="card card-back" aria-label="Card back">
    <div class="seal">
      <p class="seal-name">Bright Counsel<br>Path</p>
    </div>
  </section>
</main>
</body>
</html>
```